Business cards for education company

We need a business card design for a relatively new company based in Queensland and operating across Australia. We resell diploma level education courses which include Business, Management, Finance, Community Services & Government courses. We offer over 20 different courses.
The target market is for anyone 16 years of age and older. There is no age limit.

We would like to see the design use the color blue and silver. The final design should communicate professionalism and a bright future.

We sell education but are also promoting the career they see themselves in 2-3 years in the future

Our company logo is attached.

Target Market(s)

We target all age groups above 16 years of age. The main target market would be people aged between 17-35.

We focus on those people who cannot make it into University or do not want to commit the time to a full degree.

Industry/Entity Type

Education

Requirements
Must have
• Professional
Company logo
website
Contact details:

Please use the following example:

Lionel Parfitt
Senior Education Consultant
0417 386 591
Lionel.parfitt@brightwaylearninghub.com.au
www.brightwaylearninghub.com.au

```html
<!DOCTYPE html>
<html lang="en">
<head>
<meta charset="utf-8">
<title>Brightway Learning Hub – Business Card</title>
<link href="https://fonts.googleapis.com/css2?family=Open+Sans:wght@400;600;700&display=swap" rel="stylesheet">
<style>
  :root {
    --brand-blue: #1c4e8a;
    --accent-blue: #2f7fcf;
    --light-blue: #9cc4ec;
    --text-gray: #555a5f;
    --board-top: #f7f7f7;
    --board-bottom: #bcbcbc;
    --card-edge: #d6d6d6;
    --card-center: #fbfbfb;
  }
  * { margin: 0; padding: 0; box-sizing: border-box; }
  html, body { width: 1200px; height: 800px; overflow: hidden; }
  body {
    position: relative;
    font-family: "Open Sans", Arial, sans-serif;
    background: linear-gradient(180deg, var(--board-top) 0%, #e4e4e4 45%, var(--board-bottom) 100%);
  }

  /* Brand lockup shown on the board */
  .brand-lockup {
    position: absolute;
    left: 70px;
    top: 78px;
    display: flex;
    align-items: center;
    gap: 26px;
  }
  .brand-dot {
    width: 150px;
    height: 150px;
    border-radius: 50%;
    background: var(--accent-blue);
  }
  .brand-name {
    color: var(--brand-blue);
    font-weight: 600;
    font-size: 48px;
    line-height: 1.1;
  }

  /* Business card */
  .card {
    position: absolute;
    left: 377px;
    top: 313px;
    width: 720px;
    height: 410px;
    border: 1px solid #3a3a3a;
    background: radial-gradient(ellipse at 50% 45%, var(--card-center) 0%, #eeeeee 50%, var(--card-edge) 100%);
    box-shadow: 4px 5px 8px rgba(0,0,0,0.45);
    overflow: hidden;
  }
  .card__top-bar {
    position: absolute;
    left: 0;
    top: 0;
    width: 613px;
    height: 18px;
    background: linear-gradient(90deg, var(--accent-blue) 0%, var(--light-blue) 40%, #e9f1fa 55%, var(--light-blue) 70%, var(--accent-blue) 100%);
  }
  .card__bottom-bar {
    position: absolute;
    left: 82px;
    bottom: 0;
    right: 0;
    height: 10px;
    background: linear-gradient(90deg, var(--accent-blue) 0%, var(--light-blue) 45%, #e9f1fa 55%, var(--light-blue) 65%, var(--accent-blue) 100%);
  }

  .card__brand {
    position: absolute;
    left: 24px;
    top: 70px;
    display: flex;
    align-items: center;
    gap: 16px;
  }
  .card__brand-dot {
    width: 86px;
    height: 86px;
    border-radius: 50%;
    background: var(--accent-blue);
  }
  .card__brand-name {
    color: var(--brand-blue);
    font-weight: 600;
    font-size: 26px;
    line-height: 1.15;
  }

  .card__person {
    position: absolute;
    right: 14px;
    top: 90px;
    text-align: right;
  }
  .card__name {
    color: var(--brand-blue);
    font-weight: 700;
    font-size: 27px;
    line-height: 1.2;
  }
  .card__title {
    color: var(--text-gray);
    font-size: 24px;
    line-height: 1.25;
  }

  .card__contacts {
    position: absolute;
    left: 0;
    top: 0;
    width: 720px;
    height: 410px;
  }
  .card__contact-line {
    position: absolute;
    left: 135px;
    color: var(--brand-blue);
    font-size: 24px;
    line-height: 1;
    white-space: nowrap;
  }
  .card__contact-line--phone { top: 200px; }
  .card__contact-line--web { top: 264px; }
  .card__contact-line--mail { top: 330px; }

  .card__chart {
    position: absolute;
    left: 578px;
    top: 200px;
  }
</style>
</head>
<body>

  <div class="brand-lockup">
    <div class="brand-dot"></div>
    <div class="brand-name">Brightway<br>Learning Hub</div>
  </div>

  <div class="card">
    <div class="card__top-bar"></div>

    <div class="card__brand">
      <div class="card__brand-dot"></div>
      <div class="card__brand-name">Brightway<br>Learning Hub</div>
    </div>

    <div class="card__person">
      <div class="card__name">Lionel Parfitt</div>
      <div class="card__title">Senior Education Consultant</div>
    </div>

    <svg class="card__contacts" width="720" height="410" viewBox="0 0 720 410" aria-hidden="true">
      <line x1="83" y1="195" x2="83" y2="410" stroke="#2f7fcf" stroke-width="3"/>
      <line x1="83" y1="213" x2="118" y2="213" stroke="#2f7fcf" stroke-width="3"/>
      <line x1="83" y1="277" x2="118" y2="277" stroke="#2f7fcf" stroke-width="3"/>
      <line x1="83" y1="343" x2="118" y2="343" stroke="#2f7fcf" stroke-width="3"/>
    </svg>

    <div class="card__contact-line card__contact-line--phone">0417 386 591</div>
    <div class="card__contact-line card__contact-line--web">www.brightwaylearninghub.com.au</div>
    <div class="card__contact-line card__contact-line--mail">Lionel.parfitt@brightwaylearninghub.com.au</div>

    <svg class="card__chart" width="124" height="116" viewBox="0 0 124 116" role="img" aria-label="Pie chart">
      <g transform="translate(60 58)">
        <path d="M0 0 L0 -52 A52 52 0 0 1 45 -26 Z" fill="#e4e9f1"/>
        <path d="M0 0 L45 -26 A52 52 0 0 1 50 14 Z" fill="#d3dae6"/>
        <path d="M0 0 L50 14 A52 52 0 0 1 -8 51 Z" fill="#eef1f6"/>
        <path d="M0 0 L-8 51 A52 52 0 0 1 -52 0 Z" fill="#dde3ec"/>
        <g transform="translate(-6 -5)">
          <path d="M0 0 L-52 0 A52 52 0 0 1 0 -52 Z" fill="#c9d2e0"/>
        </g>
      </g>
    </svg>

    <div class="card__bottom-bar"></div>
  </div>

</body>
</html>
```